Stellan App | Pre-Launch Homepage

Dear designer,
Stellan is a soon to be launched innovative & free social platform for collaborative addictions quitting.
We require a design for our pre-launch homepage that will elevate our basic wireframes to the next level.
We would like the wireframes to serve as a guideline only, and not as a final version of the design. If you have cool ideas - we would appreciate your creativity!
* This is a pre-launch website for a mobile app, and as such the design must be consistent with the general style, design and atmosphere of the app (see screenshot in the shared Drive link).
* We liked the style and feel of the following website: http://plumvane.com/ - Please let's use it as a reference as well.
* The existing text in the wireframes is there just to represent a place for text. Copy will be edited by us after the design is done.
Please find the wireframes attached, and all relevant design assets and app screenshots in the following Drive shared link -
https://files.orbelink.com/open?id=7K204XqR3tPmHc8Lw2Jd61VnaGzT
Thanks,
Marcus
Industry/Entity Type
Social
Number of Pages Required
1 page
Look and feel
Each slider illustrates characteristics of the customer's brand and the style your logo design should communicate.

```html
<!DOCTYPE html>
<html lang="en">
<head>
<meta charset="utf-8">
<title>Stellan | Pre-Launch Homepage</title>
<link rel="stylesheet" href="https://fonts.googleapis.com/css2?family=Montserrat:wght@400;700&family=Lato:wght@400;700&display=swap">
<style>
:root{
  --ink-dark:#231a14;
  --ink-deep:#15100c;
  --amber:#f7b81c;
  --orange:#f39314;
  --accent:#f0a21a;
  --white:#ffffff;
  --paper:#ececec;
  --paper-light:#f6f6f6;
  --text:#5b5b5b;
  --text-muted:#9a9a9a;
  --night:#2a2826;
  --night-deep:#1d1b1a;
  --footer:#353535;
}
*{box-sizing:border-box;margin:0;padding:0}
html,body{width:1200px;height:2920px;overflow:hidden}
body{font-family:"Lato",sans-serif;color:var(--text);background:var(--white);position:relative}
section,footer{position:absolute;left:0;width:1200px;overflow:hidden}
.abs{position:absolute}
h1,h2,h3,.brand,.label,.btn{font-family:"Montserrat",sans-serif}

/* hero */
.hero{top:0;height:640px;background:linear-gradient(120deg,#4a3626 0%,var(--ink-dark) 45%,var(--ink-deep) 100%)}
.hero-photo{left:0;top:0;width:1200px;height:640px;background:radial-gradient(ellipse at 75% 45%,rgba(120,90,60,.55),rgba(0,0,0,0) 60%)}
.hero-device{left:820px;top:48px;width:280px;height:592px;border-radius:30px 30px 0 0;background:linear-gradient(160deg,#2e2e30,#0c0c0d 60%,#8a6a50)}
.brand{left:80px;top:44px;font-size:38px;font-weight:700;color:var(--amber);letter-spacing:1px;z-index:2}
.hero h1{left:80px;top:150px;width:960px;font-size:48px;line-height:58px;font-weight:700;color:var(--white);text-transform:uppercase;white-space:nowrap;z-index:2}
.hero .lead{left:80px;top:294px;width:520px;font-size:21px;line-height:30px;color:#e8e0d8;z-index:2}
.hero-form{left:80px;top:410px;width:560px;height:116px;background:rgba(0,0,0,.45);border:1px solid rgba(255,255,255,.12);padding:20px 24px;z-index:2}
.hero-form .label{font-size:12px;font-weight:700;color:var(--white);letter-spacing:.5px;text-transform:uppercase}
.field{display:flex;margin-top:18px;gap:12px}
.input{flex:1;height:40px;background:var(--white);font-size:12px;color:var(--text-muted);padding:12px 14px}
.btn{height:40px;padding:0 22px;background:var(--amber);color:var(--white);font-size:11px;font-weight:700;display:flex;align-items:center;text-transform:uppercase}
.arrow{top:380px;width:40px;height:40px;border:2px solid rgba(255,255,255,.6);border-radius:50%}
.arrow-left{left:18px}.arrow-right{left:1142px}
.hero-notch{left:580px;top:620px;width:40px;height:40px;background:#2a2018;transform:rotate(45deg)}

/* values */
.values{top:640px;height:500px;background:linear-gradient(180deg,var(--amber),var(--orange))}
.values h2{left:0;top:92px;width:1200px;text-align:center;font-size:22px;font-weight:700;color:var(--white);text-transform:uppercase;letter-spacing:.5px}
.value{top:170px;width:360px;text-align:center;color:var(--white)}
.value-art{width:130px;height:130px;border-radius:50%;margin:0 auto 30px}
.value h3{font-size:15px;font-weight:700;text-transform:uppercase}
.value p{font-size:13px;margin-top:8px;line-height:19px;color:#fff3dc}

/* fun */
.fun{top:1140px;height:460px;background:var(--paper)}
.fun-device{left:150px;top:50px;width:170px;height:340px;border-radius:22px;background:linear-gradient(160deg,#333,#0d0d0d)}
.copy h2{font-size:26px;font-weight:700;color:var(--accent);text-transform:uppercase;margin-bottom:22px}
.copy p{font-size:16px;line-height:27px;margin-bottom:18px}
.copy a{color:var(--accent);text-decoration:underline}
.fun .copy{left:530px;top:110px;width:560px}

/* inspire */
.inspire{top:1600px;height:300px;background:var(--paper-light)}
.inspire .copy{left:100px;top:80px;width:520px}
.inspire-device-a{left:830px;top:40px;width:110px;height:220px;border-radius:16px;background:linear-gradient(160deg,#2b2b2b,#0e0e0e)}
.inspire-device-b{left:930px;top:20px;width:130px;height:260px;border-radius:18px;background:linear-gradient(160deg,#f7b81c,#e9880f)}

/* achieve */
.achieve{top:1900px;height:500px;background:linear-gradient(180deg,var(--night),var(--night-deep))}
.achieve h2{left:0;top:50px;width:1200px;text-align:center;font-size:24px;font-weight:700;color:var(--white);text-transform:uppercase}
.achieve .intro{left:250px;top:100px;width:700px;text-align:center;font-size:15px;line-height:24px;color:#bdbdbd}
.achieve-phone{left:530px;top:220px;width:140px;height:280px;border-radius:20px 20px 0 0;background:var(--orange);border:10px solid #111}
.trophy{left:30px;top:60px}
.feature{width:360px;display:flex;gap:16px;font-size:14px;line-height:22px;color:#bdbdbd}
.feature svg{flex:none;margin-top:4px}

/* coming soon */
.soon{top:2400px;height:400px;background:var(--white)}
.soon h2{left:0;top:36px;width:1200px;text-align:center;font-size:24px;font-weight:700;color:var(--accent);text-transform:uppercase}
.soon-laptop{left:140px;top:120px;width:370px;height:230px;border-radius:8px;background:linear-gradient(160deg,#2a2520,#6b5038)}
.soon-form{left:560px;top:140px;width:540px;height:150px;border:1px solid #e0e0e0;padding:26px 26px}
.soon-form .label{font-size:12px;font-weight:700;color:#444;text-transform:uppercase}
.soon-form .input{border:1px solid #e3e3e3}
.soon-actions{left:530px;top:318px;display:flex;gap:16px}
.round{width:40px;height:40px;border-radius:50%;background:#8d8d8d}
.round.active{background:var(--orange)}
.dots{left:572px;top:376px;display:flex;gap:8px}
.dot{width:8px;height:8px;border-radius:50%;background:#c8c8c8}
.dot.on{background:#666}

/* footer */
footer{top:2800px;height:120px;background:var(--footer)}
.copyright{left:40px;top:52px;font-size:12px;color:#bdbdbd;text-transform:uppercase;letter-spacing:.5px}
.social{left:905px;top:44px;display:flex;gap:10px}
.social span{width:30px;height:30px;border-radius:50%}
</style>
</head>
<body>

<section class="hero">
  <div class="abs hero-photo" role="img" aria-label="Dark blurred photo backdrop of a person holding a smartphone"></div>
  <div class="abs hero-device" role="img" aria-label="Hand holding a smartphone showing the app screen"></div>
  <div class="abs brand">Stellan</div>
  <h1 class="abs">Become a better version<br>of yourself</h1>
  <p class="abs lead">Stellan is a revolutionary &amp; free social platform for collaborative addictions quitting.</p>
  <div class="abs hero-form">
    <div class="label">Subscribe below for the beta release and updates</div>
    <div class="field"><div class="input">Enter your email address</div><div class="btn">Let me know</div></div>
  </div>
  <svg class="abs arrow arrow-left" viewBox="0 0 40 40"><path d="M23 12l-8 8 8 8" fill="none" stroke="#fff" stroke-width="2"/></svg>
  <svg class="abs arrow arrow-right" viewBox="0 0 40 40"><path d="M17 12l8 8-8 8" fill="none" stroke="#fff" stroke-width="2"/></svg>
  <div class="abs hero-notch"></div>
</section>

<section class="values">
  <h2 class="abs">On the other hand, we denounce with righteous indignation</h2>
  <div class="abs value" style="left:60px">
    <div class="value-art" role="img" aria-label="Red and white lifebuoy illustration" style="background:radial-gradient(circle,#fff 0 30%,#e0332a 31% 100%)"></div>
    <h3>Never be alone network</h3>
    <p>Forget what you know – Stellan makes<br>it fun to quit</p>
  </div>
  <div class="abs value" style="left:420px">
    <div class="value-art" role="img" aria-label="Golden star illustration" style="background:radial-gradient(circle,#fde9a0,#e8b630)"></div>
    <h3>Never be alone network</h3>
    <p>Forget what you know – Stellan makes<br>it fun to quit</p>
  </div>
  <div class="abs value" style="left:780px">
    <div class="value-art" role="img" aria-label="Feathered headdress illustration" style="background:radial-gradient(circle,#ffffff,#c9c0b0)"></div>
    <h3>Stay motivated</h3>
    <p>Forget what you know – Stellan makes<br>it fun to quit</p>
  </div>
</section>

<section class="fun">
  <div class="abs fun-device" role="img" aria-label="Smartphone showing a no-smoking screen"></div>
  <div class="abs copy">
    <h2>Fun</h2>
    <p>Forget what you know – <a>Stellan makes it fun to quit</a>. The battle between your good and bad choices comes to life in an <a>gamified approach</a> thrumping your campaigns.</p>
    <p>Stellan gives you the opportunity to take on <a>Stellan life</a> or helping your beloved to <a>persist</a> your common addictions as a team. That's right, we invented the rewarded process into a social game.</p>
  </div>
</section>

<section class="inspire">
  <div class="abs copy">
    <h2>Inspire</h2>
    <p>One of the most important factors for successful quitting is the ability to stay <a>inspired</a> during the process.</p>
    <p>That's why we designed Stellan as a platform where you can inspire and be inspired by a supportive network of awesome Stellan-ers!</p>
  </div>
  <div class="abs inspire-device-a" role="img" aria-label="Dark smartphone with app screen"></div>
  <div class="abs inspire-device-b" role="img" aria-label="Smartphone with orange app screen"></div>
</section>

<section class="achieve">
  <h2 class="abs">Achieve</h2>
  <p class="abs intro">Stellan is built as a pyramid of relationships that makes use of the Social Cognitive Theory, to provide a powerful network of positive reinforcement. The bigger you make it the stronger you get.</p>
  <div class="abs achieve-phone">
    <svg class="abs trophy" width="40" height="44" viewBox="0 0 40 44"><path d="M8 2h24v12a12 12 0 0 1-24 0z M16 26h8v8h-8z M10 36h20v6H10z" fill="#fff"/></svg>
  </div>
  <div class="abs feature" style="left:110px;top:250px"><svg width="22" height="22" viewBox="0 0 22 22"><path d="M4 2h14v7a7 7 0 0 1-14 0z M9 16h4v3H9z M6 19h10v3H6z" fill="#f7b81c"/></svg><p>Stellan is built as a pyramid of relationships that makes use of the Social Cognitive Theory, to provide a powerful network of positive reinforcement.</p></div>
  <div class="abs feature" style="left:110px;top:360px"><svg width="22" height="22" viewBox="0 0 22 22"><path d="M1 3h4l3 11h11l2-8H7" fill="none" stroke="#f7b81c" stroke-width="2"/><circle cx="9" cy="18" r="2" fill="#f7b81c"/><circle cx="17" cy="18" r="2" fill="#f7b81c"/></svg><p>Stellan is built as a pyramid of relationships that makes use of the Social Cognitive Theory, to provide a powerful network of positive reinforcement.</p></div>
  <div class="abs feature" style="left:730px;top:250px"><svg width="22" height="22" viewBox="0 0 22 22"><path d="M4 2h14v7a7 7 0 0 1-14 0z M9 16h4v3H9z M6 19h10v3H6z" fill="#f7b81c"/></svg><p>Stellan is built as a pyramid of relationships that makes use of the Social Cognitive Theory, to provide a powerful network of positive reinforcement.</p></div>
  <div class="abs feature" style="left:730px;top:360px"><svg width="22" height="22" viewBox="0 0 22 22"><path d="M1 3h4l3 11h11l2-8H7" fill="none" stroke="#f7b81c" stroke-width="2"/><circle cx="9" cy="18" r="2" fill="#f7b81c"/><circle cx="17" cy="18" r="2" fill="#f7b81c"/></svg><p>Stellan is built as a pyramid of relationships that makes use of the Social Cognitive Theory, to provide a powerful network of positive reinforcement.</p></div>
</section>

<section class="soon">
  <h2 class="abs">Coming soon</h2>
  <div class="abs soon-laptop" role="img" aria-label="Laptop displaying the homepage hero"></div>
  <div class="abs soon-form">
    <div class="label">Subscribe below for the beta release and updates</div>
    <div class="field"><div class="input">Enter your email address</div><div class="btn">Let me know</div></div>
  </div>
  <div class="abs soon-actions"><span class="round"></span><span class="round"></span><span class="round active"></span></div>
  <div class="abs dots"><span class="dot on"></span><span class="dot"></span><span class="dot"></span></div>
</section>

<footer>
  <div class="abs copyright">Copyright © 2015 Stellan Ltd.</div>
  <div class="abs social">
    <span style="background:#3b5fa8"></span>
    <span style="background:#2fa8de"></span>
    <span style="background:#d6472f"></span>
    <span style="background:#f39314"></span>
    <span style="background:#e04a4a"></span>
    <span style="background:#777"></span>
  </div>
</footer>

</body>
</html>
```